Business Card Design for Vel
Fun, earthy, organic food company needs professional cards to speak our message!
Business Card Design for Vel -
Creative Brief
Bright & Fun-filled
Marcus Dell
Managing Member & Co-Founder
PO Box 482937 Dallas, TX 75318-2937
mdell@ourvelway.com
http:\\www.ourvelway.com
If you can access the closed project, we'll be using logo #84 in the folowing link: http://www.kavdrafthub.com/contests/logo-for-vel. We'll be uploading the logo file shortly for this project. We like simple, fun and creative but are open to many designs and styles.
The back of the card should be our logo colors, green and brown. It could be a cool design based off of the colors, you could use the entire length of the back with the logo or place both colors on the back with it being split with a similar design of the tree in our logo. We're open to your creativity!
quelldraw quelldraw
@KR - working on it now & submit our conmcepts soon! Thanks
Fovra Fovra
Please Check top right message box of the page.
trolen447 trolen447
Designers, We're looking to expedite the process on this. First come first serve on the card design. If you provide designs for stationary as well and we choose you, we'll provide a $50 donation to you. We're even open to selecting two winners for business card and stationary. So submit for each, because you could win for either or both! Thanks!

```html
<!DOCTYPE html>
<html lang="en">
<head>
<meta charset="utf-8">
<title>Vel Business Card</title>
<link href="https://fonts.googleapis.com/css2?family=Open+Sans:ital,wght@0,400;0,600;0,700;1,400&display=swap" rel="stylesheet">
<style>
  :root {
    --earth-brown: #4e3526;
    --earth-brown-deep: #3b271b;
    --leaf-green: #7cc142;
    --leaf-green-soft: #a6d86f;
    --paper: #ffffff;
    --ink: #5a5a5a;
    --stage: #e9e9e9;
  }
  * { box-sizing: border-box; margin: 0; padding: 0; }
  html, body { width: 1200px; height: 797px; overflow: hidden; }
  body {
    background: var(--stage);
    font-family: "Open Sans", Arial, sans-serif;
    display: flex;
    align-items: center;
    justify-content: center;
    gap: 50px;
  }
  .card {
    position: relative;
    width: 540px;
    height: 310px;
    border-radius: 14px;
    overflow: hidden;
    box-shadow: 0 10px 30px rgba(0,0,0,0.18);
  }

  /* Back */
  .card-back { background: var(--earth-brown); }
  .card-back .palm-art {
    position: absolute;
    right: 40px; top: 30px;
    width: 210px; height: 260px;
    border-radius: 50% 50% 10px 10px;
    background: radial-gradient(ellipse at 50% 35%, var(--leaf-green-soft), var(--leaf-green) 70%);
    opacity: 0.9;
  }
  .card-back .brand {
    position: absolute;
    left: 34px; bottom: 58px;
  }
  .card-back .site {
    position: absolute;
    left: 34px; bottom: 28px;
    color: var(--leaf-green);
    font-size: 12px;
  }

  /* Brand lockup */
  .brand { display: flex; align-items: center; gap: 8px; }
  .brand-square {
    width: 22px; height: 22px;
    background: var(--leaf-green);
  }
  .brand-name {
    font-weight: 700;
    font-size: 34px;
    line-height: 1;
    color: var(--leaf-green);
  }

  /* Front */
  .card-front { background: var(--paper); }
  .card-front .brand { position: absolute; left: 30px; top: 36px; }
  .card-front .brand-name { font-size: 28px; }
  .card-front .brand-square { width: 18px; height: 18px; }
  .card-front .palm-art {
    position: absolute;
    right: 30px; top: 22px;
    width: 200px; height: 240px;
    border-radius: 50% 50% 10px 10px;
    background: radial-gradient(ellipse at 50% 35%, var(--leaf-green-soft), var(--leaf-green) 70%);
  }
  .person { position: absolute; left: 30px; top: 100px; }
  .person-name {
    color: var(--leaf-green);
    font-size: 20px;
    font-weight: 600;
  }
  .person-title {
    color: var(--ink);
    font-size: 11px;
    font-style: italic;
    margin-top: 2px;
  }
  .contact { position: absolute; left: 30px; top: 160px; list-style: none; }
  .contact li {
    display: flex; align-items: flex-start; gap: 8px;
    color: var(--ink);
    font-size: 11px;
    line-height: 1.45;
    margin-bottom: 3px;
  }
  .contact svg { flex: none; margin-top: 2px; }
  .band-green {
    position: absolute; left: 0; right: 0; bottom: 14px;
    height: 6px; background: var(--leaf-green);
  }
  .band-brown {
    position: absolute; left: 0; right: 0; bottom: 0;
    height: 14px; background: var(--earth-brown);
  }
</style>
</head>
<body>

<section class="card card-back">
  <div class="palm-art" role="img" aria-label="Large green palm tree illustration"></div>
  <div class="brand">
    <span class="brand-square"></span>
    <span class="brand-name">Vel</span>
  </div>
  <p class="site">www.ourvelway.com</p>
</section>

<section class="card card-front">
  <div class="brand">
    <span class="brand-square"></span>
    <span class="brand-name">Vel</span>
  </div>
  <div class="person">
    <p class="person-name">Marcus Dell</p>
    <p class="person-title">Managing Member &amp; Co-Founder</p>
  </div>
  <ul class="contact">
    <li>
      <svg width="10" height="10" viewBox="0 0 10 10"><circle cx="5" cy="5" r="5" fill="#7cc142"/></svg>
      <span>PO Box 482937<br>Dallas, TX 75318-2937</span>
    </li>
    <li>
      <svg width="10" height="10" viewBox="0 0 10 10"><circle cx="5" cy="5" r="5" fill="#7cc142"/></svg>
      <span>214-555-0187</span>
    </li>
    <li>
      <svg width="10" height="10" viewBox="0 0 10 10"><circle cx="5" cy="5" r="5" fill="#7cc142"/></svg>
      <span>mdell@ourvelway.com</span>
    </li>
  </ul>
  <div class="palm-art" role="img" aria-label="Green palm tree illustration"></div>
  <div class="band-green"></div>
  <div class="band-brown"></div>
</section>

</body>
</html>
```